MMA fitness boot camp

We need a flyer that feels friendly and inviting to people who have never done fitness or training before. It also needs to look serious so it has the look of being a serious workout program.

We dont mind how it is set out as long as it conveys the message.

We do not want images of professional MMA fighters fighting. We like fitness training images that are relatable. eg- fit women punching or kicking a punching bag . If possible add men as well. We are aiming for men and women to do the boot camp.

The information for flyer is as below-

‘MMA Fitness Bootcamp’

Join us at Ironleaf Training Hub for our new Mixed Martial Arts Bootcamp. You will train for 4 weeks with the same fitness methods a professional fighter would use before a fight! You will get an intense and challenging workout whilst having fun. This isn’t your common boot camp held at the local park, this is unique and enjoyable!

During this 4 week period, you will be training twice a week early mornings in our Training facility.

Enjoy training in a supportive environment with an MMA fighter and qualified Master trainer pushing you every session so that you get the best out of yourself.

For more information email us at marcus@ironleaftraininghub.com.au or to book your spot with us.

or visit us at-
www.ironleaftraininghub.com

ALL FITNESS LEVELS WELCOME!

Level 1, 274 Quenby Rd. Smithfield.'

```html
<!DOCTYPE html>
<html lang="en">
<head>
<meta charset="utf-8">
<title>MMA Fitness Bootcamp Flyer</title>
<link href="https://fonts.googleapis.com/css2?family=Teko:wght@500;600&family=Arimo:wght@400;700&display=swap" rel="stylesheet">
<style>
  :root {
    --backdrop: #1b1b1b;
    --paper: #ffffff;
    --ink: #1a1616;
    --orange: #f7941d;
    --orange-deep: #e5801a;
    --white: #ffffff;
  }
  * { margin: 0; padding: 0; box-sizing: border-box; }
  html, body { width: 1040px; height: 1200px; overflow: hidden; background: var(--backdrop); }
  .canvas { position: relative; width: 1040px; height: 1200px; }
  .flyer { position: absolute; left: 268px; top: 45px; width: 522px; height: 1097px; background: var(--paper); }
  .side-band { position: absolute; background: var(--orange); width: 522px; left: 0; }
  .side-band.upper { top: 273px; height: 172px; }
  .side-band.lower { top: 697px; height: 126px; }
  .panel-shape { position: absolute; left: 0; top: 0; }
  .brand {
    position: absolute; left: 0; top: 70px; width: 522px; text-align: center;
    font-family: "Teko", sans-serif; font-weight: 600; font-size: 40px; line-height: 1;
    color: var(--orange); text-transform: uppercase;
  }
  .headline {
    position: absolute; left: 34px; top: 178px; width: 454px; text-align: center;
    font-family: "Teko", sans-serif; font-weight: 500; font-size: 48px; line-height: 1;
    color: var(--orange); letter-spacing: 0.3px;
  }
  .photo {
    position: absolute; left: 34px; top: 230px; width: 454px; height: 370px;
    background: linear-gradient(120deg, #5d5a57 0%, #8f8b86 35%, #c9a79f 55%, #b6b4b0 75%, #e6e8ea 100%);
  }
  .banner {
    position: absolute; left: 20px; top: 600px; width: 482px; height: 105px;
    background: linear-gradient(180deg, var(--orange) 0%, var(--orange-deep) 100%);
    text-align: center; color: var(--ink);
  }
  .banner .invite {
    font-family: "Teko", sans-serif; font-weight: 500; font-size: 36px; line-height: 1; margin-top: 10px;
    white-space: nowrap;
  }
  .banner .invite .lead { font-size: 44px; }
  .banner .program {
    font-family: "Arimo", sans-serif; font-weight: 700; font-size: 23.5px; line-height: 26px;
    margin-top: -2px;
  }
  .body-copy {
    position: absolute; left: 52px; top: 742px; width: 440px;
    font-family: "Arimo", sans-serif; font-size: 24px; line-height: 26px; color: var(--white);
    white-space: nowrap;
  }
  .body-copy strong { font-weight: 700; }
  .contact {
    position: absolute; left: 0; top: 1014px; width: 522px; text-align: center; color: var(--ink);
  }
  .contact .label {
    font-family: "Teko", sans-serif; font-weight: 500; font-size: 25px; line-height: 20px; color: var(--orange);
  }
  .contact .detail { font-family: "Arimo", sans-serif; font-size: 16.5px; line-height: 18px; }
  .contact .detail.site { letter-spacing: 0.4px; }
</style>
</head>
<body>
<div class="canvas">
  <div class="flyer">
    <div class="side-band upper"></div>
    <div class="side-band lower"></div>
    <svg class="panel-shape" width="522" height="1097" viewBox="0 0 522 1097" aria-hidden="true">
      <path fill="#1a1616" d="M34,90 Q34,52 54,47 Q66,120 112,152 L410,152 Q456,120 468,47 Q488,52 488,90 L488,1012 Q488,1042 466,1043 Q456,1000 420,996 L102,996 Q66,1000 56,1043 Q34,1042 34,1012 Z"/>
    </svg>
    <div class="brand">Ironleaf Training Hub</div>
    <h1 class="headline">MMA FITNESS BOOTCAMP</h1>
    <div class="photo" role="img" aria-label="Photo of a woman lifting a barbell overhead in a bright gym"></div>
    <div class="banner">
      <p class="invite"><span class="lead">JOIN US</span> AT IRONLEAF TRAINING HUB</p>
      <p class="program">FOR OUR NEW MIXED MARTIAL ARTS<br>BOOTCAMP</p>
    </div>
    <p class="body-copy">You will train for <strong>4 weeks</strong> with the<br>same fitness methods a professional<br>fighter would use before a fight! You<br>will get an intense and challenging<br>workout whilst having fun. <strong>This isn’t</strong><br><strong>your common boot camp held at</strong><br><strong>the local park, this is unique and</strong><br><strong>enjoyable!</strong></p>
    <div class="contact">
      <p class="label">FOR MORE INFORMATION EMAIL US AT</p>
      <p class="detail">marcus@ironleaftraininghub.com.au</p>
      <p class="label">VISIT OUR WEBSITE</p>
      <p class="detail site">www.ironleaftraininghub.com</p>
    </div>
  </div>
</div>
</body>
</html>
```